Wedding Music Playlist Template

Hi, I'm a wedding musician and I'd like a 1 pager wedding music template created. It needs to be editable for future weddings.

At the top of the template:
Bride First Name & Groom First Name plus 's WEDDING
Date of Wedding:
Venue name:

(The form needs to be flexible where I can remove/interchange Prelude Ceremony / Ceremony / Canapes / Reception) as sometimes I will play music just for a Ceremony sometimes for both Ceremony/Canapes or sometimes just the reception only or all of the above.

Section 1: Prelude Ceremony (this could be up to 5 songs)

Section 2: Ceremony
Processional (this is sometimes 1 or 2 songs)
Signing of Papers (this is sometimes 1 or 2 songs)
Recessional (1 song)

Section 3: Canapes

Section 4: Reception

Within each section
Artist
Song

I'd also like the template to feature
logo (attached) and social media links
website URL tomwelker.com.au
instagram: tomwelkertunes
facebook: tomwelkerkeysman
soundcloud: keysguy_ceremonies

I see the form/template serving two purposes.
1) I'll send back to the bride when she books me for a wedding and she may socialise it.
2) Posting on instagram as I perform at each wedding and attract engaged brides looking for wedding pianist or even just ideas for wedding music.

Target Market(s)

Engaged Couples looking for wedding music or suggested music for wedding

Industry/Entity Type

Wedding

Requirements
Must have
• Please see project description.
Nice to have
• Background wedding image with text overlayed

```html
<!DOCTYPE html>
<html lang="en">
<head>
<meta charset="utf-8">
<title>Wedding Music Playlist – Sophie &amp; Daniel</title>
<link rel="stylesheet" href="https://fonts.googleapis.com/css2?family=Lobster&family=Lobster+Two:ital,wght@1,700&family=Montserrat:wght@400;500;600;700&display=swap">
<style>
  :root{
    --pink-band:#eba8b0;
    --pink-row:#f7b9c1;
    --grey-row:#e8e8ea;
    --rose:#e0636d;
    --rose-link:#f4a3ad;
    --ink:#3b3335;
    --brown:#4a3a3a;
    --black:#000;
    --white:#fff;
    --gold:#6b5a3a;
    --row-h:24.5px;
  }
  *{margin:0;padding:0;box-sizing:border-box}
  html,body{width:967px;height:1200px;overflow:hidden;background:var(--white)}
  body{font-family:"Montserrat",sans-serif;color:var(--ink)}
  .sheet{position:relative;width:967px;height:1200px;overflow:hidden;background:var(--black)}
  .band-top{position:absolute;left:0;top:0;width:967px;height:646px;background:var(--pink-band)}
  .notes-top{position:absolute;left:0;top:0;width:967px;height:130px;
    background:linear-gradient(180deg,rgba(255,255,255,.22),rgba(255,255,255,0))}
  .notes-bottom{position:absolute;left:0;top:1010px;width:967px;height:190px;
    background:linear-gradient(100deg,rgba(107,90,58,.45),rgba(107,90,58,.15) 55%,rgba(107,90,58,.35))}
  .card{position:absolute;left:0;top:0}
  .abs{position:absolute}
  .title-script{left:0;width:967px;top:70px;text-align:center;font-family:"Lobster Two",cursive;font-style:italic;font-weight:700;font-size:40px;color:var(--brown);left:0;width:968px}
  .couple{left:0;width:968px;top:150px;text-align:center;font-family:"Lobster",cursive;font-size:64px;color:var(--rose);line-height:1}
  .couple .amp{font-size:38px;color:var(--brown);margin:0 8px}
  .date{left:0;width:968px;top:230px;text-align:center;font-size:20px;font-weight:500}
  .venue{left:0;width:968px;top:276px;text-align:center;font-size:14.5px}
  .section-title{font-size:16.5px;font-weight:600;text-align:center;letter-spacing:.3px}
  .sub-title{font-size:14px;font-weight:500}
  .col-labels{display:flex;justify-content:space-between;font-size:12px;padding:0 3px}
  .col-labels span:last-child{width:134px;text-align:left;padding-left:38px}
  .rows{position:relative;background:repeating-linear-gradient(180deg,var(--pink-row) 0 var(--row-h),var(--grey-row) var(--row-h) calc(var(--row-h)*2))}
  .rows::after{content:"";position:absolute;top:0;bottom:0;width:1.5px;background:var(--white)}
  .left .rows::after{left:244px}
  .right .rows::after{left:243px}
  .left{left:85px;width:378px}
  .right{left:499px;width:378px}
  .brand-mark{left:532px;top:994px;width:88px;height:88px;border:1.5px solid var(--white);border-radius:50%}
  .brand-name{left:640px;top:1021px;font-size:32px;font-weight:600;color:var(--white);letter-spacing:-.5px}
  .brand-url{left:640px;top:1074px;font-size:15.5px;font-weight:700;color:var(--rose-link)}
  .socials{left:640px;top:1106px;list-style:none;font-size:12px;color:var(--white);line-height:22px}
  .socials li{display:flex;align-items:center;gap:5px}
  .socials li::before{content:"";width:10px;height:10px;background:var(--rose-link);border-radius:2px}
</style>
</head>
<body>
<main class="sheet">
  <div class="band-top"></div>
  <div class="notes-top" role="img" aria-label="Faint musical notes and staff lines over the pink band"></div>
  <div class="notes-bottom" role="img" aria-label="Golden musical notes and treble clef flowing across the black base"></div>

  <svg class="card" width="967" height="1200" aria-hidden="true">
    <path d="M88 51 H879 A30 30 0 0 1 909 81 V934 A30 30 0 0 1 879 964 H528 A30 30 0 0 0 498 994 V1083 A30 30 0 0 1 468 1113 H88 A30 30 0 0 1 58 1083 V81 A30 30 0 0 1 88 51 Z" fill="#fff" stroke="#e0636d" stroke-width="1.5"/>
  </svg>

  <header>
    <div class="abs title-script">Wedding</div>
    <h1 class="abs couple">Sophie<span class="amp">&amp;</span>Daniel</h1>
    <p class="abs date">On July XX 2017</p>
    <p class="abs venue">St Anne's Hall, Elmstead Green, EG4 2PL , Parking in Orchard rd EG4 7QR</p>
    <svg class="abs" style="left:87px;top:300px" width="793" height="16" aria-hidden="true">
      <line x1="4" y1="8" x2="789" y2="8" stroke="#3b3335" stroke-width="1.5"/>
      <path d="M0 8 L4 4 L8 8 L4 12Z M785 8 L789 4 L793 8 L789 12Z" fill="#3b3335"/>
      <circle cx="352" cy="8" r="2.6" fill="#3b3335"/><circle cx="368" cy="8" r="2.6" fill="#3b3335"/>
      <circle cx="425" cy="8" r="2.6" fill="#3b3335"/><circle cx="441" cy="8" r="2.6" fill="#3b3335"/>
    </svg>
  </header>

  <!-- Left column -->
  <section class="abs left" style="top:345px">
    <h2 class="section-title">PRELUDE CEREMONY</h2>
    <svg width="378" height="16" style="margin-top:8px;display:block" aria-hidden="true"><use href="#divider"/></svg>
    <div class="col-labels" style="margin-top:6px"><span>Song</span><span>Artist</span></div>
    <div class="rows" style="height:122px;margin-top:2px"></div>
  </section>

  <section class="abs left" style="top:555px">
    <h2 class="section-title">CEREMONY</h2>
    <svg width="378" height="16" style="margin-top:6px;display:block" aria-hidden="true"><use href="#divider"/></svg>
    <h3 class="sub-title" style="margin-top:14px">Processional</h3>
    <div class="col-labels"><span>Song</span><span>Artist</span></div>
    <div class="rows" style="height:49px;margin-top:2px"></div>
    <h3 class="sub-title" style="margin-top:13px">Signing of Papers</h3>
    <div class="col-labels"><span>Song</span><span>Artist</span></div>
    <div class="rows" style="height:49px;margin-top:2px"></div>
    <h3 class="sub-title" style="margin-top:11px">Recessional</h3>
    <div class="col-labels"><span>Song</span><span>Artist</span></div>
    <div class="rows" style="height:49px;margin-top:2px"></div>
  </section>

  <section class="abs left" style="top:901px">
    <h2 class="section-title">CANAPES</h2>
    <svg width="378" height="16" style="margin-top:8px;display:block" aria-hidden="true"><use href="#divider"/></svg>
    <div class="col-labels" style="margin-top:10px"><span>Song</span><span>Artist</span></div>
    <div class="rows" style="height:122px;margin-top:2px"></div>
  </section>

  <!-- Right column -->
  <section class="abs right" style="top:345px">
    <h2 class="section-title">RECEPTION</h2>
    <svg width="378" height="16" style="margin-top:8px;display:block" aria-hidden="true"><use href="#divider"/></svg>
    <div class="col-labels" style="margin-top:6px"><span>Song</span><span>Artist</span></div>
    <div class="rows" style="height:515px;margin-top:2px"></div>
  </section>

  <footer>
    <div class="abs brand-mark" aria-hidden="true"></div>
    <div class="abs brand-name">TOMWELKER</div>
    <div class="abs brand-url">www.tomwelker.com.au</div>
    <ul class="abs socials">
      <li>instagram.com/tomwelkertunes</li>
      <li>facebook.com/tomwelkerkeysman</li>
      <li>soundcloud.com/keysguy_ceremonies</li>
    </ul>
  </footer>

  <svg width="0" height="0" style="position:absolute" aria-hidden="true">
    <defs>
      <g id="divider">
        <line x1="4" y1="8" x2="374" y2="8" stroke="#3b3335" stroke-width="1.5"/>
        <path d="M0 8 L4 4 L8 8 L4 12Z M370 8 L374 4 L378 8 L374 12Z" fill="#3b3335"/>
        <circle cx="146" cy="8" r="2.6" fill="#3b3335"/><circle cx="163" cy="8" r="2.6" fill="#3b3335"/>
        <circle cx="215" cy="8" r="2.6" fill="#3b3335"/><circle cx="232" cy="8" r="2.6" fill="#3b3335"/>
        <circle cx="189" cy="8" r="8.5" fill="#3b3335"/>
        <path d="M189 12 L185 8 A2.2 2.2 0 0 1 189 5.5 A2.2 2.2 0 0 1 193 8 Z" fill="#f4a3ad"/>
      </g>
    </defs>
  </svg>
</main>
</body>
</html>
```